Lumen Path - Fiber Internet to the home postcard

Design a postcard for my company, Lumen Path, using the logo below. On the front of the card:
- No Buffering • No BS
- Second line should be the logo
- $60 / month • 10-Gigs
- lumenpath.net

Color palate should follow the colors in the logo.

Address should say
- Special pricing during construction
- Our best price
- Our fastest speed
- $60 / month • 10-Gigs
- lumenpath.net

Target Market(s)

25 - 55 year olds. Middle income/class. People with kids and pick up trucks

Industry/Entity Type

Fiber Internet Service Provider

Font styles to use
Sans Serif

Colors

Designer to choose colors to be used in the design.

Requirements
Nice to have
• I am open to more creative changes

```html
<!DOCTYPE html>
<html lang="en">
<head>
<meta charset="utf-8">
<title>Lumen Path – Fiber Internet Postcard</title>
<link rel="stylesheet" href="https://fonts.googleapis.com/css2?family=Jost:wght@500;600;700&family=Archivo:wght@700;800;900&family=Oswald:wght@500&display=swap">
<style>
  :root {
    --navy: #1d2c5e;
    --green: #7ac143;
    --white: #ffffff;
    --stage: #6b6c70;
    --photo-light: #eef0ee;
    --photo-mid: #9fd85a;
    --photo-warm-1: #e6d6c6;
    --photo-warm-2: #8a5a3e;
  }
  * { box-sizing: border-box; margin: 0; padding: 0; }
  html, body { width: 1200px; height: 532px; overflow: hidden; }
  body { background: var(--stage); position: relative; }

  .postcard {
    position: absolute;
    top: 84px;
    width: 510px;
    height: 364px;
    background: var(--white);
    overflow: hidden;
    box-shadow: 4px 6px 10px rgba(0,0,0,.35);
  }
  .postcard--front { left: 70px; font-family: "Jost", sans-serif; }
  .postcard--back { left: 619px; font-family: "Archivo", sans-serif; }

  .postcard__art { position: absolute; inset: 0; width: 510px; height: 364px; z-index: 2; }

  .brand {
    position: absolute;
    left: 30px;
    top: 52px;
    height: 48px;
    display: flex;
    align-items: center;
    gap: 10px;
    color: var(--navy);
    font-weight: 700;
    font-size: 42px;
    line-height: 1;
    letter-spacing: -0.5px;
    white-space: nowrap;
    z-index: 3;
  }
  .postcard--back .brand { font-weight: 800; font-size: 38px; }
  .brand__dot { width: 40px; height: 40px; border-radius: 50%; background: var(--green); flex: none; }

  /* Front */
  .perks {
    position: absolute;
    right: 25px;
    top: 22px;
    text-align: right;
    font-family: "Oswald", sans-serif;
    font-weight: 500;
    font-size: 20px;
    line-height: 30px;
    color: var(--navy);
    z-index: 3;
  }
  .perks__item { display: flex; justify-content: flex-end; align-items: center; gap: 6px; }
  .perks__item svg { width: 16px; height: 16px; }

  .offer-band {
    position: absolute;
    left: 0;
    width: 226px;
    background: var(--navy);
    border-top-right-radius: 22px;
    z-index: 1;
  }
  .offer-band--price { top: 135px; height: 82px; }
  .offer-band--speed { top: 226px; height: 81px; }
  .offer-band__value {
    position: absolute;
    left: 30px;
    top: 2px;
    color: var(--green);
    font-weight: 600;
    font-size: 66px;
    line-height: 1;
    letter-spacing: -1px;
  }
  .offer-band--speed .offer-band__value { left: 48px; }
  .offer-band__unit {
    position: absolute;
    right: 0;
    bottom: 0;
    background: var(--green);
    color: var(--navy);
    font-weight: 500;
    font-size: 17px;
    padding: 3px 10px 2px 14px;
    border-top-left-radius: 12px;
  }

  .site-url--front {
    position: absolute;
    left: 47px;
    top: 318px;
    font-size: 22px;
    font-weight: 500;
    color: var(--navy);
    z-index: 3;
  }

  /* Back */
  .site-url--back {
    position: absolute;
    right: 17px;
    top: 20px;
    font-weight: 800;
    font-size: 22px;
    color: var(--navy);
    z-index: 3;
  }
  .promo-note {
    position: absolute;
    left: 31px;
    top: 128px;
    color: var(--green);
    font-weight: 800;
    font-size: 16px;
    line-height: 20px;
    z-index: 3;
  }
  .feature-band {
    position: absolute;
    left: 0;
    width: 270px;
    background: linear-gradient(110deg, var(--green) 0%, #8fcf5a 45%, var(--green) 70%);
    z-index: 1;
  }
  .feature-band--price { top: 182px; height: 78px; }
  .feature-band--speed { top: 265px; height: 77px; }
  .feature-band__label {
    position: absolute;
    left: 31px;
    top: 12px;
    color: var(--navy);
    font-weight: 800;
    font-size: 16px;
  }
  .feature-band__value {
    position: absolute;
    left: 30px;
    top: 30px;
    color: var(--navy);
    font-weight: 900;
    font-size: 29px;
  }
</style>
</head>
<body>

<section class="postcard postcard--front">
  <div class="offer-band offer-band--price">
    <span class="offer-band__value">$60</span>
    <span class="offer-band__unit">Month</span>
  </div>
  <div class="offer-band offer-band--speed">
    <span class="offer-band__value">10</span>
    <span class="offer-band__unit">Gigs</span>
  </div>

  <svg class="postcard__art" viewBox="0 0 510 364">
    <defs>
      <radialGradient id="front-photo-tone" cx="60%" cy="55%" r="60%">
        <stop offset="0%" stop-color="var(--photo-mid)"/>
        <stop offset="55%" stop-color="#cfe6b4"/>
        <stop offset="100%" stop-color="var(--photo-light)"/>
      </radialGradient>
    </defs>
    <circle cx="505" cy="300" r="268" fill="var(--navy)"/>
    <circle cx="527" cy="300" r="250" fill="url(#front-photo-tone)" role="img" aria-label="Photo of a surprised woman in a green top holding a smartphone"/>
    <path d="M269 0 H510 V114 C430 114 320 86 269 0 Z" fill="var(--navy)"/>
    <path d="M269 0 H510 V100 C430 102 320 74 269 0 Z" fill="var(--green)"/>
  </svg>

  <div class="brand"><span>Lumen Path</span><span class="brand__dot"></span></div>

  <div class="perks">
    <div class="perks__item">
      <svg viewBox="0 0 16 16"><circle cx="8" cy="8" r="6.5" fill="none" stroke="var(--navy)" stroke-width="2"/><path d="M4.8 8.2 L7.2 10.5 L11.3 5.6" fill="none" stroke="var(--navy)" stroke-width="2"/></svg>
      <span>NO BUFFERING</span>
    </div>
    <div class="perks__item">
      <svg viewBox="0 0 16 16"><circle cx="8" cy="8" r="6.5" fill="none" stroke="var(--navy)" stroke-width="2"/><path d="M4.8 8.2 L7.2 10.5 L11.3 5.6" fill="none" stroke="var(--navy)" stroke-width="2"/></svg>
      <span>NO BS</span>
    </div>
  </div>

  <div class="site-url site-url--front">lumenpath.net</div>
</section>

<section class="postcard postcard--back">
  <div class="feature-band feature-band--price">
    <span class="feature-band__label">OUR BEST PRICE</span>
    <span class="feature-band__value">$60 / month</span>
  </div>
  <div class="feature-band feature-band--speed">
    <span class="feature-band__label">OUR FASTEST SPEED</span>
    <span class="feature-band__value">10-Gigs</span>
  </div>

  <svg class="postcard__art" viewBox="0 0 510 364">
    <defs>
      <linearGradient id="back-photo-tone" x1="0" y1="0" x2="1" y2="1">
        <stop offset="0%" stop-color="var(--photo-warm-1)"/>
        <stop offset="60%" stop-color="#c9a88e"/>
        <stop offset="100%" stop-color="var(--photo-warm-2)"/>
      </linearGradient>
    </defs>
    <circle cx="505" cy="300" r="268" fill="var(--navy)"/>
    <circle cx="527" cy="300" r="250" fill="url(#back-photo-tone)" role="img" aria-label="Photo of a smiling father and daughter using a laptop on a living room sofa"/>
    <path d="M269 0 H510 V114 C430 114 320 86 269 0 Z" fill="var(--navy)"/>
    <path d="M269 0 H510 V100 C430 102 320 74 269 0 Z" fill="var(--green)"/>
  </svg>

  <div class="brand"><span>Lumen Path</span><span class="brand__dot"></span></div>
  <div class="site-url site-url--back">lumenpath.net</div>

  <p class="promo-note">SPECIAL PRICING<br>DURING CONSTRUCTION</p>
</section>

</body>
</html>
```